Design home page for brightvane.xyz

We’re seeking a sleek, lead-generation-focused single-page website for Brightvane.xyz that communicates our expertise in delivering high-intent leads to mid-sized businesses. The goal is to guide visitors toward scheduling a free consultation while emphasizing our performance-based approach and comprehensive service offerings.

Industry/Entity Type

Marketing

Number of Pages Required

1 page

Font styles to use
Sans Serif

Requirements
Must have
• content from https://files.quorvalet.example/doc/7hTmwQRZa93KpLdVyxNe42UcBsFoGj8rYiMn5EkPtWz/view?tab=t.0
Nice to have
• color pallet from here https://files.quorvalet.example/doc/4pRkz-NWb62VxLeTyqJs8cHaDmFu3GiYoBnQ5tXeKv/view?tab=t.0

```html
<!DOCTYPE html>
<html lang="en">
<head>
<meta charset="utf-8">
<title>Brightvane.xyz — High-Quality Leads</title>
<link rel="stylesheet" href="https://fonts.googleapis.com/css2?family=Inter:wght@400;500;600;700&display=swap">
<style>
  :root {
    --ink: #0d0d0d;
    --muted: #6f6f6f;
    --brand: #686285;
    --brand-soft: #b7b1c9;
    --brand-text: #7a7592;
    --paper: #ffffff;
  }
  * { box-sizing: border-box; margin: 0; padding: 0; }
  html, body { width: 693px; height: 1200px; overflow: hidden; background: var(--paper); }
  body { font-family: "Inter", sans-serif; color: var(--ink); position: relative; }

  .process-title {
    position: absolute; top: 62px; left: 0; width: 693px;
    text-align: center; font-size: 23px; font-weight: 700; letter-spacing: -0.2px;
  }
  .process-intro {
    position: absolute; left: 23px; top: 214px; width: 280px;
    font-size: 14.5px; line-height: 17.8px; color: var(--brand);
  }
  .timeline { position: absolute; left: 344px; top: 150px; width: 30px; height: 195px; }
  .step { position: absolute; left: 377px; width: 300px; }
  .step h3 { font-size: 14.5px; font-weight: 600; line-height: 18px; }
  .step p { color: var(--muted); margin-top: 7px; }
  .step-1 { top: 155px; }
  .step-1 p, .step-3 p { font-size: 12.4px; line-height: 15.2px; }
  .step-2 { top: 238px; }
  .step-2 p { font-size: 10.5px; line-height: 13px; margin-top: 5px; }
  .step-3 { top: 321px; }

  .apart {
    position: absolute; left: 0; top: 486px; width: 693px; height: 301px;
    background: var(--brand); border-radius: 14px;
  }
  .apart h2 {
    position: absolute; top: 17px; width: 100%; text-align: center;
    font-size: 14.5px; font-weight: 700;
  }
  .apart .lede {
    position: absolute; top: 39px; width: 100%; text-align: center; font-size: 10.3px;
  }
  .card {
    position: absolute; top: 77px; width: 206px; height: 158px;
    background: var(--brand-soft); border-radius: 14px;
    box-shadow: 0 2px 4px rgba(40,35,70,0.25);
    padding: 44px 10px 0 10px;
  }
  .card h3 { font-size: 14.5px; font-weight: 700; color: var(--brand); line-height: 18px; }
  .card p { font-size: 10.5px; line-height: 13px; color: var(--brand-text); margin-top: 6px; }
  .card-1 { left: 19px; }
  .card-2 { left: 244px; padding-left: 11px; }
  .card-3 { left: 468px; }

  .growth-photo {
    position: absolute; left: 19px; top: 886px; width: 327px; height: 261px;
    border-radius: 14px; box-shadow: 0 1px 4px rgba(0,0,0,0.2);
    background: linear-gradient(160deg, #e9e8e7 0%, #c9c3bb 45%, #8a7a68 75%, #4a4440 100%);
  }
  .growth-copy { position: absolute; left: 383px; top: 917px; width: 300px; }
  .growth-copy h2 { font-size: 14.5px; line-height: 17.8px; font-weight: 700; color: var(--brand); }
  .growth-copy h3 { font-size: 14.5px; font-weight: 600; margin-top: 8px; line-height: 18px; }
  .growth-copy p { font-size: 10.5px; line-height: 13px; color: var(--muted); margin-top: 6px; width: 275px; }
  .growth-copy .first { margin-left: 1px; }
</style>
</head>
<body>
  <h1 class="process-title">How We Deliver High-Quality Leads</h1>
  <p class="process-intro">Our streamlined process ensures you receive ready-to-engage leads without the hassle</p>

  <svg class="timeline" viewBox="0 0 30 195" aria-hidden="true">
    <g fill="none" stroke="#686285" stroke-width="0.6" stroke-dasharray="3 2">
      <line x1="14" y1="26" x2="14" y2="85"/>
      <line x1="14" y1="109" x2="14" y2="168"/>
      <circle cx="14" cy="14" r="11.5"/>
      <circle cx="14" cy="97" r="11.5"/>
      <circle cx="14" cy="179" r="11.5"/>
    </g>
    <g fill="#686285">
      <circle cx="14" cy="14" r="9"/>
      <circle cx="14" cy="97" r="9"/>
      <circle cx="14" cy="179" r="9"/>
    </g>
  </svg>

  <div class="step step-1">
    <h3>Precis Market Targeting</h3>
    <p>We start understanding your ideal customer profile and identifying high-intent prospects in your market.</p>
  </div>
  <div class="step step-2">
    <h3>Customized Campaign Execution</h3>
    <p>We take the time to understand your audience, creating and running campaigns tailored to their interests leveraging insights from advertising, SEO, and lead magnets.</p>
  </div>
  <div class="step step-3">
    <h3>All-Inclusive Management</h3>
    <p>From strategy to execution, we handle every detail, delivering leads while you focus on closing deals.</p>
  </div>

  <section class="apart">
    <h2>Whats Sets Us Apart?</h2>
    <p class="lede">We're more than just a lead generation service our approach ensures valuable opportunities for your business.</p>
    <div class="card card-1">
      <h3>High-Intent Leads</h3>
      <p>The high-intent leads we generate provide a solid starting point for building meaningful connections.</p>
    </div>
    <div class="card card-2">
      <h3>Complete Service</h3>
      <p>We take care of everything needed to generate leads, so you can stay focused on growing your business</p>
    </div>
    <div class="card card-3">
      <h3>Success-Based Partnership</h3>
      <p>With our results driven model, you pay only for the leads we deliver, ensuring value every step of the way</p>
    </div>
  </section>

  <div class="growth-photo" role="img" aria-label="Photo of a team meeting around a table in a bright office"></div>
  <div class="growth-copy">
    <h2>Effortless Growth, Designed for you We simplify lead generation, so you can focus on growing your business</h2>
    <h3 class="first">Hands-off convenience</h3>
    <p>We manage the strategy, content, advertising, and optimization,delivering a steady flow of high-quality prospects.</p>
    <h3>Built to scale</h3>
    <p>Our process adapts to your growth goals, ensuring consistent lead flow whether you're starting small or scaling rapidly.</p>
  </div>
</body>
</html>
```